Business Card Design Project

We need a business card for our IT services provider business. We provide services to small and medium business, and would like something that reflects the color scheme / branding on our recently updated website - www.tallobrix.com.au

The card type we have chosen is a matte laminated double sided configuration at 86mm x 54mm on 350 GSM cardboard.
Updates

Target Market(s)

Small and Medium Business owners

Industry/Entity Type

Business

Requirements
Must have
• *Details on all cards*

Company Name: Tallobrix Pty Ltd
ABN: 52 683 914 207
Address: 47-49 Pembury Street, Ashcombe Vale, Victoria 3172
Phone: 1300 GRAB UP
Fax: 03 9417 6258
Website: www.tallobrix.com.au
Logo/Handprint Icon

*Person Specific*

```html
<!DOCTYPE html>
<html lang="en">
<head>
<meta charset="utf-8">
<title>Tallobrix Business Card</title>
<link rel="stylesheet" href="https://fonts.googleapis.com/css2?family=Arimo:wght@400;700&display=swap">
<style>
  :root {
    --stage: #1c1d20;
    --card-white: #f4f4f4;
    --brand-blue: #1b5e9e;
    --brand-blue-light: #2870b3;
    --brand-blue-dark: #134f88;
    --ink: #222222;
    --white: #ffffff;
  }
  * { margin: 0; padding: 0; box-sizing: border-box; }
  html, body {
    width: 1200px; height: 984px; overflow: hidden;
    background: var(--stage);
    font-family: "Arimo", Arial, sans-serif;
  }
  .canvas {
    width: 1200px; height: 984px;
    display: flex; flex-direction: column;
    align-items: center; justify-content: center; gap: 44px;
  }
  .card {
    width: 700px; height: 440px; position: relative; overflow: hidden;
    border-radius: 3px;
    box-shadow: 0 12px 30px rgba(0,0,0,0.5);
  }

  /* Front: white card with contact details */
  .card-front { background: linear-gradient(160deg, var(--white), var(--card-white)); }
  .front-logo {
    position: absolute; left: 48px; top: 56px;
    display: flex; align-items: center; gap: 12px;
    font-size: 46px; font-weight: 400; color: var(--ink); letter-spacing: 1px;
  }
  .logo-mark { width: 18px; height: 18px; border-radius: 50%; background: var(--brand-blue); }
  .person {
    position: absolute; right: 40px; top: 50px; text-align: right;
  }
  .person-name {
    font-size: 30px; font-weight: 700; color: var(--brand-blue); margin-bottom: 14px;
  }
  .person-line {
    display: flex; justify-content: flex-end; align-items: center; gap: 10px;
    font-size: 19px; color: var(--ink); margin-bottom: 8px;
  }
  .person-line svg { width: 18px; height: 16px; }
  .details-band {
    position: absolute; left: 0; right: 0; bottom: 0; height: 170px;
    background: linear-gradient(180deg, var(--brand-blue-light), var(--brand-blue));
    color: var(--white); padding: 30px 40px 0 0; text-align: right;
    font-size: 20px; line-height: 1.6;
  }
  .details-band b { font-weight: 700; }
  .sep { margin: 0 10px; opacity: 0.85; }

  /* Back: blue card with name and web address */
  .card-back {
    background: linear-gradient(150deg, var(--brand-blue-light), var(--brand-blue-dark));
    color: var(--white);
  }
  .back-logo {
    position: absolute; left: 0; right: 0; top: 150px; text-align: center;
    display: flex; justify-content: center; align-items: center; gap: 18px;
    font-size: 88px; font-weight: 400; letter-spacing: 3px;
  }
  .back-logo .logo-mark { width: 26px; height: 26px; background: var(--white); }
  .web-address {
    position: absolute; left: 0; right: 0; top: 300px; text-align: center;
    font-size: 24px; letter-spacing: 2px;
  }
  .web-address b { font-weight: 700; }
  .web-rule {
    position: absolute; left: 200px; width: 300px; top: 290px; height: 2px;
    background: linear-gradient(90deg, rgba(255,255,255,0), rgba(255,255,255,0.9), rgba(255,255,255,0));
  }
</style>
</head>
<body>
<main class="canvas">
  <section class="card card-front">
    <div class="front-logo"><span class="logo-mark"></span>Tallobrix</div>
    <div class="person">
      <p class="person-name">Marcus HALE</p>
      <p class="person-line">1300 482 915
        <svg viewBox="0 0 18 16" aria-hidden="true"><rect x="5" y="1" width="8" height="14" rx="1.5" fill="none" stroke="#1b5e9e" stroke-width="1.6"/><circle cx="9" cy="12" r="1" fill="#1b5e9e"/></svg>
      </p>
      <p class="person-line">marcus@tallobrix.com.au
        <svg viewBox="0 0 18 16" aria-hidden="true"><rect x="1" y="3" width="16" height="11" fill="none" stroke="#1b5e9e" stroke-width="1.6"/><path d="M1 3 L9 9 L17 3" fill="none" stroke="#1b5e9e" stroke-width="1.6"/></svg>
      </p>
    </div>
    <div class="details-band">
      <p><b>Tallobrix Pty Ltd</b><span class="sep">|</span>ABN: 52 683 914 207</p>
      <p>47-49 Pembury Street, Ashcombe Vale, Victoria 3172</p>
      <p><b>Phone:</b> 1300 GRAB UP<span class="sep">|</span><b>Fax:</b> 03 9417 6258</p>
    </div>
  </section>

  <section class="card card-back">
    <div class="back-logo"><span class="logo-mark"></span>Tallobrix</div>
    <div class="web-rule"></div>
    <p class="web-address">www.<b>tallobrix</b>.com.au</p>
  </section>
</main>
</body>
</html>
```